Invitation - Melbourne Show Invitation

We need an e-Invitation for our Trade Show in Melbourne. We are holding a furniture show at our Melbourne Showroom:

The Brindlewood Private Show

Dates: Wednesday 19th to Friday 21st July

Hours: 9am to 6pm

Join us for Drinks on Thursday 20th from 5pm

Address:
The Lantern Room
47 Dunmore Street
Melbourne

RSVP: rosalind@brindlewood-au.com

Tel. 03 9555 0182

The style of the building and the furniture is mid-century design, so I would like the invitation to reflect this (think "Tin Harbor").

Target Market(s)

Professional Retailers

Industry/Entity Type

Trade

Font styles to use
Sans Serif

Colors

Designer to choose colors to be used in the design.

Requirements
Must have
• Dates and Times

```html
<!DOCTYPE html>
<html lang="en">
<head>
<meta charset="utf-8">
<title>The Brindlewood Private Show – Invitation</title>
<link rel="stylesheet" href="https://fonts.googleapis.com/css2?family=Oranienbaum&display=swap">
<style>
  :root {
    --page-bg: #e9e9e9;
    --panel-dark: #2b2a29;
    --band-dark: #1c1c1c;
    --ink-light: #f4f2ee;
    --ink-soft: #e6e3dd;
    --accent-gold: #b98a4e;
    --photo-light: #f3f2ef;
    --photo-mid: #d9d6d0;
    --photo-floor: #c9a77e;
  }
  * { margin: 0; padding: 0; box-sizing: border-box; }
  html, body { width: 830px; height: 1200px; overflow: hidden; }
  body {
    background: var(--page-bg);
    font-family: "Oranienbaum", "Times New Roman", serif;
    position: relative;
  }
  .invitation {
    position: absolute;
    left: 0;
    top: 286px;
    width: 830px;
    height: 627px;
    overflow: hidden;
  }
  .showroom-photo {
    position: absolute;
    left: 0; top: 0;
    width: 417px; height: 627px;
    background: linear-gradient(180deg,
      var(--photo-light) 0%,
      var(--photo-light) 45%,
      var(--photo-mid) 62%,
      var(--photo-floor) 82%,
      var(--photo-light) 100%);
  }
  .brand-band {
    position: absolute;
    left: 0; top: 37px;
    width: 417px; height: 92px;
    background: var(--band-dark);
    display: flex;
    align-items: center;
    padding-left: 38px;
    gap: 18px;
  }
  .brand-mark {
    width: 54px; height: 54px;
    border: 3px solid var(--ink-light);
    border-radius: 6px;
  }
  .brand-name {
    color: var(--ink-light);
    font-size: 50px;
    line-height: 1;
  }
  .details-panel {
    position: absolute;
    left: 417px; top: 0;
    width: 413px; height: 627px;
    background: var(--panel-dark);
    color: var(--ink-light);
    text-align: center;
  }
  .show-title { position: absolute; left: 0; width: 100%; top: 62px; line-height: 1; font-weight: 400; }
  .show-title span { display: block; }
  .title-the { font-size: 58px; }
  .title-name { font-size: 74px; margin-top: 4px; }
  .title-sub { font-size: 54px; margin-top: 4px; }
  .show-dates {
    position: absolute; left: 0; width: 100%; top: 318px;
    font-size: 22px; line-height: 25px; color: var(--ink-soft);
  }
  .show-hours { display: block; margin-top: 8px; }
  .show-drinks { display: block; margin-top: 8px; font-size: 18px; line-height: 22px; }
  .divider-ornament {
    position: absolute; left: 96px; top: 478px;
    width: 220px; height: 8px;
    background: var(--accent-gold);
    border-radius: 4px;
  }
  .show-contact {
    position: absolute; left: 0; width: 100%; top: 512px;
    font-size: 17px; line-height: 1.2; color: var(--ink-soft);
    white-space: nowrap;
  }
  .show-venue { margin-top: 16px; font-size: 18px; }
</style>
</head>
<body>
  <main class="invitation">
    <div class="showroom-photo" role="img" aria-label="Bright white mid-century showroom with tall windows, a timber dining table and black chairs on a light wooden floor"></div>
    <div class="brand-band">
      <span class="brand-mark"></span>
      <span class="brand-name">Brindlewood</span>
    </div>
    <section class="details-panel">
      <h1 class="show-title">
        <span class="title-the">The</span>
        <span class="title-name">Brindlewood</span>
        <span class="title-sub">Private Show</span>
      </h1>
      <p class="show-dates">
        Wednesday 19th<br>to<br>Friday 21st July
        <span class="show-hours">9am to 6pm</span>
        <span class="show-drinks">Join us for Drinks Thursday 20th from 5pm</span>
      </p>
      <div class="divider-ornament" role="img" aria-label="Gold decorative flourish divider"></div>
      <div class="show-contact">
        <p>RSVP: rosalind@brindlewood-au.com | Tel: 03 9555 0182</p>
        <p class="show-venue">The Lantern Room 47 Dunmore Street Melbourne</p>
      </div>
    </section>
  </main>
</body>
</html>
```